fairway fox drywall repair web page

need a web presence for my company. we are a golf themed drywall repair company. need a home page, contact us, photos, about us, services possible payment option

```html
<!DOCTYPE html>
<html lang="en">
<head>
<meta charset="utf-8">
<title>Fairway Fox Drywall Repair</title>
<link href="https://fonts.googleapis.com/css2?family=Ubuntu:wght@300;400;500;700&display=swap" rel="stylesheet">
<style>
:root{
  --navy:#1f2a6b;
  --gold:#d6a228;
  --panel:#f3f3f3;
  --body-text:#8c8c8c;
  --white:#ffffff;
  --sky-top:#8a8e92;
  --sky-warm:#d6a672;
  --grass:#3f6a22;
  --grass-dark:#24410f;
}
*{margin:0;padding:0;box-sizing:border-box}
html,body{width:1036px;height:1200px;overflow:hidden}
body{position:relative;font-family:'Ubuntu',sans-serif;color:var(--navy)}
.backdrop{position:absolute;inset:0;
  background:linear-gradient(180deg,var(--sky-top) 0%,var(--sky-warm) 22%,#b79a6a 36%,var(--grass) 52%,var(--grass-dark) 85%,#2f4f18 100%)}
.quick-call{position:absolute;top:24px;right:102px;font-size:12px;color:#f5f0e6;display:flex;align-items:center;gap:4px}
.quick-call strong{font-weight:500;color:var(--white)}
.quick-call span{font-weight:300}
.page{position:absolute;left:100px;top:54px;width:835px;height:1024px;background:var(--white)}
.site-header{height:95px;position:relative}
.brand{position:absolute;left:18px;top:30px;display:flex;align-items:center;gap:8px;font-size:17px;font-weight:500;color:var(--navy)}
.brand-dot{width:14px;height:14px;border-radius:50%;background:var(--gold)}
.main-nav{position:absolute;top:40px;left:0;width:100%;font-size:13px}
.main-nav a{position:absolute;color:var(--navy);text-decoration:none;white-space:nowrap}
.main-nav a.active{color:var(--gold)}
.hero{position:absolute;left:0;top:95px;width:835px;height:461px;
  background:linear-gradient(120deg,#e9e9e7 0%,#d3d2ce 40%,#c4c2bd 65%,#eef0f0 100%)}
.hero-title{position:absolute;left:0;width:100%;top:334px;text-align:center;font-size:30px;font-weight:300;color:var(--navy);letter-spacing:-.3px}
.hero-arrow{position:absolute;top:300px}
.card{position:absolute;top:605px;width:256px;height:382px;background:var(--panel)}
.card h2{position:absolute;left:16px;top:26px;font-size:21px;font-weight:400;color:var(--navy);letter-spacing:-.3px}
.photo-block{position:absolute}
.body-copy{font-size:9.5px;font-weight:300;color:var(--body-text);line-height:17px}
.about-text{position:absolute;left:13px;top:198px;width:232px}
.service{position:absolute;left:14px;width:236px}
.service-icon{position:absolute;left:0;top:0;width:40px;height:40px;border-radius:50%;background:var(--gold);display:flex;align-items:center;justify-content:center}
.service h3{position:absolute;left:46px;top:11px;font-size:13px;font-weight:300;color:var(--navy)}
.service p{position:absolute;left:48px;top:30px;width:190px}
.photo-caption{position:absolute;left:13px;top:250px;width:236px}
.site-footer{position:absolute;top:1102px;left:0;width:1036px;text-align:center;color:var(--white)}
.footer-nav{font-size:13px;word-spacing:2px}
.footer-nav a{color:var(--white);text-decoration:none}
.footer-nav .sep{margin:0 12px}
.copyright{margin-top:14px;font-size:13px}
</style>
</head>
<body>
<div class="backdrop" role="img" aria-label="Blurred golf course at sunset with a golf ball near the cup"></div>

<div class="quick-call">
  <svg width="10" height="10" viewBox="0 0 24 24"><path fill="#1f2a6b" d="M6.6 10.8a15 15 0 0 0 6.6 6.6l2.2-2.2a1 1 0 0 1 1-.25 11.4 11.4 0 0 0 3.6.57 1 1 0 0 1 1 1V20a1 1 0 0 1-1 1A17 17 0 0 1 3 4a1 1 0 0 1 1-1h3.5a1 1 0 0 1 1 1c0 1.25.2 2.45.57 3.57a1 1 0 0 1-.25 1z"/></svg>
  <strong>Quick Call Now !</strong><span>1-800-555-0147</span>
</div>

<div class="page">
  <header class="site-header">
    <div class="brand"><span class="brand-dot"></span>Fairway Fox</div>
    <nav class="main-nav">
      <a class="active" href="#" style="left:444px">Home</a>
      <a href="#" style="left:510px">About Us</a>
      <a href="#" style="left:594px">Photos</a>
      <a href="#" style="left:666px">Services</a>
      <a href="#" style="left:746px">Contact Us</a>
    </nav>
  </header>

  <section class="hero" role="img" aria-label="Worker smoothing joint compound on a drywall panel beside a window">
    <svg class="hero-arrow" style="left:44px" width="20" height="32" viewBox="0 0 20 32"><path d="M16 4 L5 16 L16 28" fill="none" stroke="#d6a228" stroke-width="3"/></svg>
    <svg class="hero-arrow" style="left:772px" width="20" height="32" viewBox="0 0 20 32"><path d="M4 4 L15 16 L4 28" fill="none" stroke="#d6a228" stroke-width="3"/></svg>
    <h1 class="hero-title">Fairway Fox Drywall Repair</h1>
  </section>

  <section class="card" style="left:10px">
    <h2>ABOUT US</h2>
    <div class="photo-block" role="img" aria-label="Contractor in a hard hat drilling into drywall" style="left:14px;top:59px;width:230px;height:128px;background:linear-gradient(135deg,#9aa0a6,#4a4f56 60%,#2e3238)"></div>
    <p class="body-copy about-text">Lorem Ipsum is simply dummy text of the printing and typesetting industry. Lorem Ipsum has been the industry's standard dummy text ever since the 1500s, when an unknown printer took a galley of type and scrambled it to make a type specimen book. It has survived not only five centuries, but also the leap into electronic typesetting, remaining essentially unchanged.</p>
  </section>

  <section class="card" style="left:290px">
    <h2>SERVICES</h2>
    <div class="service" style="top:74px">
      <div class="service-icon"><svg width="18" height="18" viewBox="0 0 24 24"><path fill="#fff" d="M21 6.5a5 5 0 0 1-6.6 4.7L6 19.6a2 2 0 0 1-2.8-2.8l8.4-8.4A5 5 0 0 1 17.5 2l-3 3 .5 3 3 .5 3-3z"/></svg></div>
      <h3>Repair</h3>
      <p class="body-copy">Lorem Ipsum is simply dummy text of the printing and typesetting industry. Lorem Ipsum has been the industry's</p>
    </div>
    <div class="service" style="top:175px">
      <div class="service-icon"><svg width="18" height="18" viewBox="0 0 24 24"><path fill="#fff" d="M9 3h6a1 1 0 0 1 1 1v2h4a1 1 0 0 1 1 1v12a1 1 0 0 1-1 1H4a1 1 0 0 1-1-1V7a1 1 0 0 1 1-1h4V4a1 1 0 0 1 1-1zm1 3h4V5h-4z"/><path d="M8 13l3 3 5-6" fill="none" stroke="#d6a228" stroke-width="2"/></svg></div>
      <h3>Installing</h3>
      <p class="body-copy">Lorem Ipsum is simply dummy text of the printing and typesetting industry. Lorem Ipsum has been the industry's</p>
    </div>
    <div class="service" style="top:272px">
      <div class="service-icon"><svg width="18" height="18" viewBox="0 0 24 24"><path d="M5 3h11l3 3v15H5z" fill="none" stroke="#fff" stroke-width="2"/><path d="M8 9h8M8 13h8M8 17h5" stroke="#fff" stroke-width="1.8"/></svg></div>
      <h3>Finishing</h3>
      <p class="body-copy">Lorem Ipsum is simply dummy text of the printing and typesetting industry. Lorem Ipsum has been the industry's</p>
    </div>
  </section>

  <section class="card" style="left:569px">
    <h2>PHOTOS</h2>
    <div class="photo-block" role="img" aria-label="Hands applying plaster to a wall with a putty knife" style="left:13px;top:59px;width:229px;height:185px;background:linear-gradient(135deg,#dcdad6,#bdbab4 55%,#a8a59f)"></div>
    <p class="body-copy photo-caption">Lorem Ipsum is simply dummy text of the printing and typesetting industry.t Lorem Ipsum</p>
    <div class="photo-block" role="img" aria-label="Scraper on an orange wall" style="left:13px;top:298px;width:65px;height:51px;background:linear-gradient(135deg,#e6b26a,#c9803a)"></div>
    <div class="photo-block" role="img" aria-label="Hand patching around an outlet" style="left:96px;top:298px;width:65px;height:51px;background:linear-gradient(135deg,#cfc6ba,#a99c8c)"></div>
    <div class="photo-block" role="img" aria-label="Trowel spreading compound" style="left:177px;top:298px;width:65px;height:51px;background:linear-gradient(135deg,#b9cbe0,#8aa3c2)"></div>
  </section>
</div>

<footer class="site-footer">
  <nav class="footer-nav">
    <a href="#">Home</a><span class="sep">|</span><a href="#">About Us</a><span class="sep">|</span><a href="#">Photos</a><span class="sep">|</span><a href="#">Services</a><span class="sep">|</span><a href="#">Contact Us</a>
  </nav>
  <p class="copyright">© 2015 Company Name , All Rights Reserved</p>
</footer>
</body>
</html>
```